2026 Varnex Loprin LWB Vehicle Wrap Design for Ridgeway Electrical and Refrigeration Work Vans

We are Ridgeway Electrical and Refrigeration — a Perth-based commercial electrical, air conditioning and refrigeration company. We service commercial buildings, homes and luxury residential jobs across the metro area and remote WA.
We need a clean, professional and high-impact full vehicle wrap design for our work vans. The vans are our mobile billboards, so the design needs to look sharp from a distance, communicate trust and competence, and clearly show what we do.
Must include:

Our company name: Ridgeway Electrical and Refrigeration
Tagline options (you can choose the strongest placement or suggest alternatives):
“Electrical | Air Conditioning | Refrigeration – Perth & Remote WA”
Licence numbers "AU051237 and EC24813"
Phone number: 0491 538 214
Website: ridgewayelectricalrefrigeration.com.au
Email: admin@ridgewayelectricalrefrigeration.com.au
Our existing logo (will be uploaded)

Style we want:

Professional, modern and trustworthy
Bold enough to stand out on the road but not flashy or overly busy
Clean hierarchy so the company name and phone number are readable at speed
Strong use of contrast

Colour preferences:

Prefer designs that work with our existing branding (we will upload the logo and brand colours)
Open to strong, professional colour combinations (navy/dark blue, black, white, and one accent colour such as orange, red or electric blue often work well in the trades)

Avoid:

Cluttered designs with too much text
Cartoonish or overly “tradie” looking graphics
Designs that look cheap or dated

Additional notes:

Design should scale well so we can use the same concept across multiple vans
We will need print-ready files (high-res, layered) at the end

Please upload your best concepts. We will give clear feedback and work with the winning designer to refine the final artwork for production.

Target Market(s)

commercial buildings, homes and luxury residential jobs across the metro area and remote WA.

Industry/Entity Type

Electrical, Air Conditioning and Refrigeration

Colors
0054AA
0677BA
7BADD7
CADEEF
E8F1F8

Requirements
Must have
• Our company name: Ridgeway Electrical and Refrigeration Tagline options (you can choose the strongest placement or suggest alternatives): “Electrical | Air Conditioning | Refrigeration – Perth & Remote WA” Licence numbers "AU051237 and EC24813" Phone number: 0491 538 214 Website: ridgewayelectricalrefrigeration.com.au Email: admin@ridgewayelectricalrefrigeration.com.au Our existing logo (will be uploaded)
Nice to have
• Professional, modern and trustworthy Bold enough to stand out on the road but not flashy or overly busy Clean hierarchy so the company name and phone number are readable at speed Strong use of contrast
Should not have
• Cluttered designs with too much text Cartoonish or overly “tradie” looking graphics Designs that look cheap or dated

```html
<!DOCTYPE html>
<html lang="en">
<head>
<meta charset="utf-8">
<title>Ridgeway Electrical and Refrigeration – Van Wrap Layout</title>
<link rel="stylesheet" href="https://fonts.googleapis.com/css2?family=Montserrat:wght@800&family=Oswald:wght@400;500&display=swap">
<style>
  :root {
    --wrap-blue: #0E62C4;
    --brand-deep: #0054AA;
    --wrap-white: #EEF0EC;
    --page: #FFFFFF;
    --head-font: "Montserrat", Arial, sans-serif;
    --line-font: "Oswald", "Arial Narrow", sans-serif;
  }
  html, body {
    margin: 0;
    width: 1200px;
    height: 1200px;
    overflow: hidden;
    background: var(--page);
  }
  .canvas { position: relative; width: 1200px; height: 1200px; }
  .panel { position: absolute; }
  .panel svg { position: absolute; inset: 0; }
  .txt { position: absolute; margin: 0; white-space: nowrap; }

  .headline {
    font-family: var(--head-font);
    font-weight: 800;
    color: var(--wrap-blue);
    line-height: 1;
    text-transform: uppercase;
  }
  .phone {
    font-family: var(--head-font);
    font-weight: 800;
    line-height: 1;
  }
  .tagline {
    font-family: var(--line-font);
    font-weight: 400;
    text-transform: uppercase;
    letter-spacing: 0.3px;
    line-height: 1.25;
  }
  .contact {
    font-family: var(--line-font);
    font-weight: 500;
    text-transform: uppercase;
    font-size: 10px;
    display: flex;
    align-items: center;
    gap: 6px;
  }
  .contact .dot {
    width: 11px; height: 11px; border-radius: 50%;
    display: inline-block;
  }
  .licence {
    font-family: var(--line-font);
    font-weight: 400;
    text-transform: uppercase;
    text-align: center;
    font-size: 10px;
    line-height: 1.35;
  }
  .brand-name {
    font-family: var(--head-font);
    font-weight: 800;
    color: var(--wrap-white);
    line-height: 1;
  }

  /* side panel */
  .side { left: 88px; top: 138px; width: 1030px; height: 356px; }
  .side .headline { left: 52px; top: 74px; font-size: 27px; }
  .side .phone { left: 50px; top: 184px; font-size: 33px; color: var(--wrap-white); }
  .side .logo-box { position: absolute; left: 322px; top: 47px; width: 218px; height: 205px; background: var(--wrap-blue); display: flex; align-items: center; justify-content: center; }
  .side .logo-box .brand-name { font-size: 31px; }
  .side .tagline { left: 310px; top: 265px; width: 242px; text-align: center; font-size: 15px; color: var(--wrap-white); }
  .side .contact { color: var(--wrap-white); }
  .side .contact .dot { background: var(--wrap-white); }
  .side .web { left: 587px; top: 196px; }
  .side .mail { left: 587px; top: 218px; }
  .side .licence { left: 808px; top: 194px; width: 130px; color: var(--wrap-white); }

  /* rear panel */
  .rear { left: 110px; top: 675px; width: 412px; height: 312px; }
  .rear .logo-box { position: absolute; left: 38px; top: 31px; width: 102px; height: 100px; background: var(--wrap-blue); display: flex; align-items: center; justify-content: center; }
  .rear .logo-box .brand-name { font-size: 16px; }
  .rear .headline { left: 159px; top: 40px; font-size: 21px; }
  .rear .phone { left: 159px; top: 96px; font-size: 27px; color: var(--wrap-blue); }
  .rear .contact { color: var(--wrap-blue); font-size: 8px; }
  .rear .contact .dot { background: var(--wrap-blue); width: 9px; height: 9px; }
  .rear .web { left: 18px; top: 154px; }
  .rear .mail { left: 202px; top: 154px; }
  .rear .licence { left: 300px; top: 210px; width: 80px; font-size: 8px; color: var(--wrap-blue); }
  .rear .tagline { left: 0; top: 275px; width: 412px; text-align: center; font-size: 12.5px; color: var(--wrap-white); }

  /* front panel */
  .front { left: 648px; top: 675px; width: 430px; height: 200px; }
  .front .logo-box { position: absolute; left: 108px; top: 127px; width: 70px; height: 36px; background: var(--wrap-blue); display: flex; align-items: center; justify-content: center; }
  .front .logo-box .brand-name { font-size: 10px; }
  .front .headline { left: 188px; top: 133px; font-size: 12px; }
</style>
</head>
<body>
<main class="canvas">

  <!-- side elevation -->
  <section class="panel side" aria-label="Side wrap artwork">
    <svg width="1030" height="356" viewBox="0 0 1030 356">
      <rect x="0" y="0" width="1030" height="356" rx="26" fill="var(--wrap-blue)"/>
      <rect x="0" y="14" width="305" height="158" fill="var(--wrap-white)"/>
      <rect x="0" y="226" width="305" height="14" fill="var(--wrap-white)"/>
      <rect x="310" y="35" width="242" height="229" fill="var(--wrap-white)"/>
    </svg>
    <h1 class="txt headline">Electrical &amp;<br>Refrigeration</h1>
    <p class="txt phone">0491 538 214</p>
    <div class="logo-box"><span class="brand-name">RIDGEWAY</span></div>
    <p class="txt tagline">Electrical | Air Conditioning<br>Refrigeration – Perth &amp; Remote WA</p>
    <p class="txt contact web"><span class="dot"></span>ridgewayelectricalrefrigeration.com.au</p>
    <p class="txt contact mail"><span class="dot"></span>admin@ridgewayelectricalrefrigeration.com.au</p>
    <p class="txt licence">LIC#<br>AU051237 &amp; EC24813</p>
  </section>

  <!-- rear elevation -->
  <section class="panel rear" aria-label="Rear wrap artwork">
    <svg width="412" height="312" viewBox="0 0 412 312">
      <rect x="0" y="0" width="412" height="312" rx="18" fill="var(--wrap-blue)"/>
      <rect x="0" y="20" width="412" height="237" fill="var(--wrap-white)"/>
      <rect x="0" y="178" width="412" height="8" fill="var(--wrap-blue)" opacity="0.15"/>
    </svg>
    <div class="logo-box"><span class="brand-name">RIDGEWAY</span></div>
    <h2 class="txt headline">Electrical &amp;<br>Refrigeration</h2>
    <p class="txt phone">0491 538 214</p>
    <p class="txt contact web"><span class="dot"></span>ridgewayelectricalrefrigeration.com.au</p>
    <p class="txt contact mail"><span class="dot"></span>admin@ridgewayelectricalrefrigeration.com.au</p>
    <p class="txt licence">LIC#<br>AU051237 &amp; EC24813</p>
    <p class="txt tagline">Electrical | Air Conditioning | Refrigeration – Perth &amp; Remote WA</p>
  </section>

  <!-- front elevation -->
  <section class="panel front" aria-label="Front wrap artwork">
    <svg width="430" height="200" viewBox="0 0 430 200">
      <rect x="0" y="0" width="430" height="200" rx="18" fill="var(--wrap-blue)"/>
      <polygon points="52,110 378,110 402,196 28,196" fill="var(--wrap-white)"/>
      <polygon points="30,100 44,100 14,196 0,196" fill="var(--wrap-white)"/>
      <polygon points="386,100 400,100 430,196 416,196" fill="var(--wrap-white)"/>
    </svg>
    <div class="logo-box"><span class="brand-name">RIDGEWAY</span></div>
    <h2 class="txt headline">Electrical &amp;<br>Refrigeration</h2>
  </section>

</main>
</body>
</html>
```